Update existing Product Data Sheets with new design / multi page layout

We are looking to update the design for our products data sheets. Here is a link to our most popular product http://www.corvantel-power.com/products/12v-100ah-lithium-ion-battery/

I am also attaching the current data sheet. Most of the information on the new data sheet will come from what is on our website.

Industry/Entity Type

Product

Requirements
Must have
• Clean, simple and corporate look. multi page design, two or more pages.
Nice to have
• would like to put infographics in place of some content if possible.

```html
<!DOCTYPE html>
<html lang="en">
<head>
<meta charset="utf-8">
<title>Material Safety Data Sheet – Corvantel</title>
<link href="https://fonts.googleapis.com/css2?family=Open+Sans:wght@400;600;700;800&display=swap" rel="stylesheet">
<style>
  :root {
    --green: #1fa33f;
    --green-text: #3aaa48;
    --ink: #2b2b2b;
    --body: #3a3a3a;
    --navy: #1b2c6b;
    --navy-deep: #0f1e55;
    --bg-center: #f4f5f6;
    --bg-edge: #cde5f4;
    --footer-value: #cfeecf;
  }
  * { margin: 0; padding: 0; box-sizing: border-box; }
  html, body { width: 927px; height: 1200px; overflow: hidden; }
  body {
    position: relative;
    font-family: "Open Sans", Arial, sans-serif;
    color: var(--body);
    background: radial-gradient(ellipse at 50% 45%, var(--bg-center) 45%, var(--bg-edge) 100%);
  }
  .brand-block { position: absolute; left: 0; top: 54px; width: 69px; height: 109px; background: var(--green); }
  .brand-name {
    position: absolute; left: 84px; top: 126px;
    display: flex; align-items: center; gap: 6px;
    font-weight: 800; font-size: 17px; letter-spacing: -0.3px; color: var(--ink);
  }
  .brand-name .mark { width: 10px; height: 10px; background: var(--green); }
  .banner {
    position: absolute; left: 254px; top: 54px; width: 673px; height: 109px;
    background: linear-gradient(100deg, var(--navy-deep) 0%, var(--navy) 45%, #2a4f93 80%, #3a6aab 100%);
  }
  .banner-title {
    position: absolute; right: 56px; top: 122px;
    color: #fff; font-weight: 700; font-size: 28.5px; letter-spacing: 0.2px;
  }
  .section { position: absolute; width: 400px; border-top: 5px solid var(--green); padding-top: 10px; }
  .col-left { left: 54px; }
  .col-right { left: 473px; width: 399px; }
  .section-no { font-size: 13.5px; color: var(--body); line-height: 1.3; }
  .section-title { font-size: 17px; font-weight: 600; color: var(--green-text); line-height: 1.3; margin-bottom: 6px; }
  .section p { font-size: 13.6px; line-height: 21px; margin-bottom: 4px; }
  .subhead { font-size: 14.4px; color: var(--ink); line-height: 22px; margin-bottom: 5px; }
  .transport p { font-size: 13.2px; line-height: 18.4px; margin-bottom: 6px; }
  .transport b { font-weight: 600; color: var(--ink); }
  .transport ul { list-style: none; }
  .transport li { position: relative; padding-left: 27px; font-size: 13.2px; line-height: 18.4px; margin-bottom: 6px; }
  .transport li::before { content: "•"; position: absolute; left: 0; }
  .laws { list-style: none; margin-top: -2px; }
  .laws li { font-size: 13.4px; line-height: 21px; padding-left: 16px; text-indent: -12px; margin-bottom: 4.6px; }
  .additional p { font-size: 13.2px; line-height: 18.4px; }
  .footer-rule { position: absolute; left: 0; top: 1081px; width: 927px; height: 5px; background: #111; }
  .footer {
    position: absolute; left: 0; top: 1092px; width: 927px; height: 108px;
    background: var(--green); color: #fff; font-size: 13px; line-height: 18.3px;
  }
  .footer dl { position: absolute; top: 12px; display: grid; }
  .footer .left { left: 63px; grid-template-columns: 109px 250px; }
  .footer .right { left: 493px; grid-template-columns: 157px 220px; }
  .footer dd { color: var(--footer-value); }
</style>
</head>
<body>
  <div class="brand-block"></div>
  <div class="brand-name"><span>CORVANTEL</span><span class="mark"></span></div>
  <div class="banner" role="img" aria-label="Dark blue abstract technology pattern banner"></div>
  <h1 class="banner-title">MATERIAL SAFETY DATA SHEET</h1>

  <section class="section col-left" style="top:201px">
    <div class="section-no">Section — 12</div>
    <h2 class="section-title">Ecological Information</h2>
    <p>When promptly used or disposed the battery does not present environmental hazard.</p>
    <p>When disposed, keep away from water, rain and snow.</p>
  </section>

  <section class="section col-left" style="top:344px">
    <div class="section-no">Section — 13</div>
    <h2 class="section-title">Disposal Considerations</h2>
    <div class="subhead">APPROPRIATE METHOD OF DISPOSAL OF SUBSTANCE OF PREPARATION</div>
    <p>If batteries are still fully charged or only partially discharged, they can be considered a reactive hazardous waste because of signif-icant amount of uncreated or unconsumed lithium remaining in the spent battery. The batteries must be neutralized through an approved secondary treatment facility prior to disposal as a hazardous waste. Recycling of battery can be done in authorized facility, through licensed waste carrier.</p>
  </section>

  <section class="section col-left transport" style="top:619px">
    <div class="section-no">Section — 14</div>
    <h2 class="section-title">Transport Information</h2>
    <p><b>IMDG Proper Shipping Name:</b> Lithium Ion Batteries</p>
    <p><b>Hazard Class:</b> Calss 9-“Dangerous Goods” for international air and ocean shipments.</p>
    <p><b>UN No.:</b> UN3480</p>
    <p><b>Packaging group:</b> II</p>
    <p>Watt-hour exceeds the standard, so it belongs to dangerous goods.</p>
    <p>When transporting or moving the battery within your installation, please follow the guidelines below:</p>
    <ul>
      <li>Make sure that all cables and external connectors are disconnected and removed from the battery prior to moving it.</li>
      <li>The packages should be in strong packaging for support during transportation. Take in a cargo of them without falling, dropping, and breakage. Prevent collapse of cargo piles and wet by rain.</li>
      <li>Avoid throwing, rolling and excessive stacking during loading and transpiration.</li>
    </ul>
  </section>

  <section class="section col-right" style="top:201px">
    <div class="section-no">Section — 15</div>
    <h2 class="section-title">Regulatory Information</h2>
    <div class="subhead">Law Information</div>
    <ul class="laws">
      <li>《Dangerous Goods Regulation》</li>
      <li>《Recommendations on the Transport of Dangerous Goods Model Regulations》</li>
      <li>《International Maritime Dangerous Goods》</li>
      <li>《Technical Instructions for the Safe Transport of Dangerous Goods》</li>
      <li>《Classification and code of dangerous goods》</li>
      <li>《Occupational Safety and Health Act》(OSHA)</li>
      <li>《Toxic Substances Control Act》(TSCA)</li>
      <li>《Consumer Product Safety Act》(CPSA)</li>
      <li>《Federal Environmental Pollution Control Act》(FEPCA)</li>
      <li>《The Oil Pollution Act》(OPA)</li>
      <li>《Superfund Amendments and Reauthorization Act Title III (302/311/312/313)》(SARA)</li>
      <li>《Resource Conservation and Recovery Act》(RCRA)</li>
      <li>《Safety Drinking Water Act》(CWA)</li>
      <li>《California Proposition 65》</li>
      <li>《Code of Federal Regulations》(CFR)</li>
    </ul>
    <p style="font-size:13.4px">In accordance with all Federal, State and Local laws.</p>
  </section>

  <section class="section col-right additional" style="top:772px">
    <div class="section-no">Section — 16</div>
    <h2 class="section-title">Additional Information</h2>
    <p>The above information is based on the data of which we are aware and is believed to be correct as of the data hereof. Since this information may be applied under conditions beyond our control and with which may be unfamiliar and since data made available subsequent to the data hereof may suggest modifications of the information, we do not assume any responsibility for the results of its use. This information is furnished upon condition that the person receiving it shall make his own determination of the suitability of the material for his particular purpose.</p>
  </section>

  <div class="footer-rule"></div>
  <footer class="footer">
    <dl class="left">
      <dt>Manufacturer:</dt><dd>Halvren Energy Co., Ltd</dd>
      <dt>Address:</dt><dd>No. 24, Qiaolin East Road, Longhe<br>New district, Shenzhen, China.</dd>
      <dt>Post Code:</dt><dd>518026</dd>
    </dl>
    <dl class="right">
      <dt>Tel:</dt><dd>+86-0755-61240387</dd>
      <dt>Emergency Telephone:</dt><dd>+86-0755-61240392</dd>
      <dt>Fax:</dt><dd>+86-0755-61240395</dd>
      <dt>E-mail:</dt><dd>contact@halvren-energy.com</dd>
    </dl>
  </footer>
</body>
</html>
```